Financial Sevices firm looking for Brochure design

Our company Veltmoor Capital and Holdings Limited (VeltHoldings)
i
Is an investment/advisory firm - www.veltholdings-grp.net
We invest in the energy sector in Africa and offer advisory services to Energy companies looking to invest in Africa. From oil and gas, to renewables (wind/solar). We are more focused on the "West African" Sub region
We need corporate brochure (Booklet style) to circulate to our corporate clients
We would like to see a design that considers the colours in our Logo (see website)
HI Guys, sorry been travelling. Seen some very good submissions and will be sending updates shortly
Reason: Dear Designers,
Thank you for participating in this project and for some of the great designs i've received so far. Unfortunately, due to the holidays, it has been difficult to consult with other members of my team. As a result, the project deadline is extended by about 12 days
I appreciate your understanding in the situation and looking forward to continuing the excellent collaboration in the coming days
Reason: Hi All,
Apologies for the multiple deadline extensions and thanks so much for all the designs which my team and I will be reviewing today and tomorrow.
We will be closing this project tomorrow by 6pm GMT (17th Jan 2014)
Thanks to all those that submitted such wonderful designs and goodluck!!
Project to be closed finally on 17th Jan 2014 at 6pm GMT
Banks, Investment Firms, Energy companies, Private Equity Funds
I have attached a Brochure that I created myself as an example of the type of information required but please also feel free to visit our website www.veltholdings-grp.net
Looking for any creative ideas you have to suplement the information provided.
Financial

```html
<!DOCTYPE html>
<html lang="en">
<head>
<meta charset="UTF-8">
<title>VeltHoldings – Sample Transactions</title>
<link href="https://fonts.googleapis.com/css2?family=Arvo:wght@700&family=Libre+Baskerville:wght@400;700&display=swap" rel="stylesheet">
<style>
  :root {
    --bg-base: #c8cdd3;
    --bg-light: #dde1e5;
    --grid-line: rgba(255,255,255,0.45);
    --panel: #58585a;
    --panel-text: #ffffff;
    --accent-red: #e3141b;
    --accent-shadow: #2a1a1a;
    --label-bg: rgba(60,60,66,0.85);
  }
  * { margin: 0; padding: 0; box-sizing: border-box; }
  html, body { width: 1200px; height: 600px; overflow: hidden; }
  body {
    position: relative;
    background:
      repeating-linear-gradient(90deg, transparent 0 157px, var(--grid-line) 157px 159px),
      repeating-linear-gradient(0deg, transparent 0 196px, var(--grid-line) 196px 198px),
      radial-gradient(ellipse at 40% 30%, var(--bg-light), var(--bg-base) 80%);
    font-family: "Libre Baskerville", Georgia, serif;
  }
  .section-title {
    position: absolute;
    right: 902px;
    top: 483px;
    text-align: right;
    font-family: "Arvo", "Rockwell", serif;
    font-weight: 700;
    font-size: 30px;
    line-height: 32px;
    color: var(--accent-red);
    text-shadow: 2px 2px 0 var(--accent-shadow);
  }
  .sector-photo {
    position: absolute;
    top: 21px;
    height: 182px;
  }
  .photo-oil { left: 307px; width: 285px;
    background: linear-gradient(180deg, #4f8fd6 0%, #a9c9ee 45%, #6e9a3e 62%, #8a7a4e 82%, #6b5a36 100%); }
  .photo-power { left: 607px; width: 286px;
    background: linear-gradient(180deg, #2f6fc8 0%, #7fb0e6 55%, #b8b6a4 78%, #8d8a6a 100%); }
  .photo-renew { left: 906px; width: 285px;
    background: linear-gradient(180deg, #7d8ea5 0%, #c7d3df 40%, #5c6a7c 70%, #4d8f2e 100%); }
  .photo-label {
    position: absolute;
    left: 163px;
    top: 81px;
    padding: 4px 5px;
    background: var(--label-bg);
    color: #fff;
    font-family: Arial, Helvetica, sans-serif;
    font-size: 8.5px;
    white-space: nowrap;
    border-radius: 2px;
  }
  .transaction-card {
    position: absolute;
    top: 203px;
    height: 397px;
    background: var(--panel);
    color: var(--panel-text);
  }
  .card-oil { left: 328px; width: 251px; }
  .card-power { left: 625px; width: 250px; }
  .card-renew { left: 923px; width: 250px; }
  .card-heading {
    font-weight: 700;
    font-size: 15.5px;
    text-align: center;
    margin-top: 38px;
    white-space: nowrap;
  }
  .card-oil .card-heading { text-align: left; padding-left: 65px; }
  .card-body {
    margin-top: 26px;
    padding-left: 29px;
    font-size: 15.5px;
    line-height: 24.6px;
    white-space: nowrap;
  }
  .card-power .card-body { padding-left: 35px; }
  .card-renew .card-body { padding-left: 30px; }
</style>
</head>
<body>
  <div class="sector-photo photo-oil" role="img" aria-label="Oil pump jack in a green field under a blue sky">
    <span class="photo-label">Project Finance Advisory Services</span>
  </div>
  <div class="sector-photo photo-power" role="img" aria-label="Thermal power plant with cooling towers and chimneys"></div>
  <div class="sector-photo photo-renew" role="img" aria-label="Solar panels and wind turbines on grassland"></div>

  <section class="transaction-card card-oil">
    <h2 class="card-heading">Oil and Gas</h2>
    <p class="card-body">Service Provider for an<br>indigenous oil &amp; gas<br>development company<br>contracted by the<br>Nigerian Government to<br>promote industrial<br>development around the<br>oil &amp; gas sector.</p>
  </section>

  <section class="transaction-card card-power">
    <h2 class="card-heading">Conventional Power</h2>
    <p class="card-body">Financial Adviser to a<br>local power company<br>developing a thermal<br>power plant to boost<br>national generating<br>capacity.</p>
  </section>

  <section class="transaction-card card-renew">
    <h2 class="card-heading">Renewables / Cleantech</h2>
    <p class="card-body">West Africa Adviser and<br>Service Provider to an<br>international specialized<br>fund manager investing<br>in renewable energy and<br>clean technology projects<br>across Africa.</p>
  </section>

  <h1 class="section-title">Sample<br>Transactions</h1>
</body>
</html>
```